IT Tradingsystem for car dealers needs Business Card Design

We need a fresh and modern design for our new business cards.

We develop a it-business system for car dealers in Sweden, Norway and on our way down to further countries in Europe, hence the namechange to Brovento Nordic AB. The site can be found at www.brovento.example. The startpage is also in for an update/modernization soon so don't take to much from here.

We are looking to print double sided, 4-colour cards.

We want to look professional, modern and serious. Open to cooler suggestions, but not too crazy. We need to make a good and serious impression on our potential customers. It needs to reflect our scandinavian design values and layout.

Preferably with the full Brovento logo in good size on the back, so the small print on the logo can be read easily.

Text that needs to go on the cards:
-------

Otto Sigurd Hamberg
Founder

Direct +46 70-512 96 44
Support 08-527 93 214
os.hamberg@brovento.example

Brovento Nordic AB
Box 7816
111 48 Stockholm

Brovento.example
Vagnkollen.example

--------
Good luck and thanks!

PS. If you need more input or see what our previous cards looked like, don't hesitate to contact me!

Target Market(s)

Decision makers / executives at brand cardealers

Industry/Entity Type

Automotive

Contact Information for Business Card

Normal size

Requirements
Must have
• Full logo
Nice to have
• Base on our orange colors
Should not have
• No fonts with serif, and not too much graphics

```html
<!DOCTYPE html>
<html lang="sv">
<head>
<meta charset="utf-8">
<title>Brovento Nordic AB – Business Card</title>
<link rel="stylesheet" href="https://fonts.googleapis.com/css2?family=Montserrat:wght@400;500;600;800&display=swap">
<style>
  :root {
    --bg: #2b2b2d;
    --card-dark: #050505;
    --card-light: #ffffff;
    --orange: #f07c22;
    --ink: #111111;
    --ink-soft: #2a2a2a;
    --white: #ffffff;
  }
  * { margin: 0; padding: 0; box-sizing: border-box; }
  html, body { width: 1200px; height: 900px; overflow: hidden; }
  body {
    background: var(--bg);
    font-family: "Montserrat", Arial, sans-serif;
    position: relative;
  }
  .card {
    position: absolute;
    left: 260px;
    width: 680px;
    height: 390px;
    border-radius: 22px;
    overflow: hidden;
  }
  .card--back { top: 45px; background: var(--card-dark); }
  .card--front { top: 465px; background: var(--card-light); }

  /* Brand lockup */
  .brand { position: absolute; }
  .brand__row { display: flex; align-items: center; gap: 14px; }
  .brand__square { width: 40px; height: 40px; background: var(--orange); }
  .brand__name {
    font-weight: 800;
    font-size: 64px;
    letter-spacing: -2px;
    line-height: 1;
    white-space: nowrap;
  }
  .brand__tagline {
    font-weight: 500;
    font-size: 15px;
    margin-top: 6px;
    letter-spacing: 0.2px;
    white-space: nowrap;
  }
  .card--back .brand { right: 52px; bottom: 52px; color: var(--white); }
  .card--back .brand__tagline { margin-left: 54px; }
  .card--front .brand { left: 40px; top: 48px; color: var(--ink); }
  .card--front .brand__name { font-size: 52px; }
  .card--front .brand__tagline { font-size: 13px; }

  /* Person */
  .person {
    position: absolute;
    right: 40px;
    top: 48px;
    width: 270px;
    text-align: right;
  }
  .person__name { color: var(--orange); font-weight: 600; font-size: 19px; white-space: nowrap; }
  .person__rule { height: 2px; background: var(--orange); width: 100%; margin: 6px 0 5px; }
  .person__title { color: var(--ink-soft); font-size: 14px; font-weight: 500; }

  /* Contact */
  .contact {
    position: absolute;
    left: 40px;
    top: 188px;
    color: var(--ink);
    font-size: 15px;
    line-height: 1.45;
  }
  .contact__company {
    color: var(--orange);
    font-weight: 600;
    font-size: 16px;
    padding-bottom: 4px;
    border-bottom: 2px solid var(--orange);
    display: inline-block;
    padding-right: 40px;
    margin-bottom: 6px;
  }
  .contact__list { list-style: none; margin-top: 4px; }
  .contact__list li { display: flex; align-items: center; gap: 12px; }
  .contact__icon { width: 12px; height: 12px; flex: none; }
  .accent { color: var(--orange); font-weight: 600; }
</style>
</head>
<body>

  <section class="card card--back" aria-label="Card back">
    <div class="brand">
      <div class="brand__row">
        <span class="brand__square"></span>
        <span class="brand__name">Brovento</span>
      </div>
      <p class="brand__tagline">Provkörd | Remarketing | vagnkollen.example</p>
    </div>
  </section>

  <section class="card card--front" aria-label="Card front">
    <div class="brand">
      <span class="brand__name">Brovento</span>
      <p class="brand__tagline">Provkörd | Remarketing | vagnkollen.example</p>
    </div>

    <div class="person">
      <p class="person__name">Otto Sigurd Hamberg</p>
      <div class="person__rule"></div>
      <p class="person__title">Founder</p>
    </div>

    <div class="contact">
      <p class="contact__company">Brovento Nordic AB</p>
      <p>Box 7816</p>
      <p>111 48 Stockholm</p>
      <ul class="contact__list">
        <li>
          <svg class="contact__icon" viewBox="0 0 12 12"><path fill="#f07c22" d="M2.3 0.8 4 2.6 3.2 4.1C3.8 5.5 5 6.8 6.6 7.6L8 6.8 11.2 8.4 10.6 10.8C5.5 11 0.9 6.4 1 1.4Z"/></svg>
          <span>+46 70-512 96 44</span>
        </li>
        <li>
          <svg class="contact__icon" viewBox="0 0 12 12"><path fill="#f07c22" d="M1 3.5C3 1.5 9 1.5 11 3.5L10 5 8 4.5 8 3.8C6.8 3.4 5.2 3.4 4 3.8L4 4.5 2 5Z"/><rect x="2.5" y="6" width="7" height="5" rx="1" fill="#f07c22"/></svg>
          <span>08-527 93 214</span>
        </li>
        <li>
          <svg class="contact__icon" viewBox="0 0 12 12"><rect x="0.8" y="2.3" width="10.4" height="7.4" rx="1" fill="none" stroke="#f07c22" stroke-width="1.4"/><path d="M1 2.8 6 6.6 11 2.8" fill="none" stroke="#f07c22" stroke-width="1.4"/></svg>
          <span>os.hamberg@brovento.example</span>
        </li>
        <li>
          <svg class="contact__icon" viewBox="0 0 12 12"><circle cx="6" cy="6" r="5.2" fill="none" stroke="#f07c22" stroke-width="1.4"/><ellipse cx="6" cy="6" rx="2.2" ry="5.2" fill="none" stroke="#f07c22" stroke-width="1.1"/><line x1="0.8" y1="6" x2="11.2" y2="6" stroke="#f07c22" stroke-width="1.1"/></svg>
          <span>www.<span class="accent">Brovento</span>.example</span>
        </li>
      </ul>
    </div>
  </section>

</body>
</html>
```